Brightstep Foot Care Advertisement Sandwich board

We need a Sandwich board design for our fungal nail clinic - please find attached the sandwich board dimensions.

The sandwich board itself will be displayed outside of a large health clinic and we need it to attract the attention of people walking by. We need a brochure holder included in the design which will hold our brochures which provides as clients with more information (please see attached also).

We are open to the designers creativity but we would like a similar theme portrayed on our board that is similar to our website (www.brightstepfootcare.co.nz) and brochure that incorporates our logo which I have attached). The final design should communicate professionalism and be a minimalist look but modern to capture the attention of pedestrians.

Finally, we would like the website and phone number (07) 312 5840.

We look forward to seeing your work.

```html
<!DOCTYPE html>
<html lang="en">
<head>
<meta charset="utf-8">
<title>Brightstep Foot Care – Sandwich Board</title>
<link rel="stylesheet" href="https://fonts.googleapis.com/css2?family=Noto+Serif:wght@400;700&family=Source+Sans+3:wght@600;700&display=swap">
<style>
  :root {
    --page-bg: #e9e9ec;
    --brand-blue: #3a64ad;
    --brand-blue-dark: #2f5597;
    --paper: #ffffff;
    --swoosh-grey: #b4b4b8;
    --pill-grey: #7b7b7f;
    --pill-grey-light: #919195;
    --ink: #2b2b2b;
    --black: #0c0c0c;
    --photo-light: #f7f6f4;
    --photo-skin: #efd9cc;
  }
  * { margin: 0; padding: 0; box-sizing: border-box; }
  html, body {
    width: 720px;
    height: 1200px;
    overflow: hidden;
    background: var(--page-bg);
  }
  .canvas {
    position: relative;
    width: 720px;
    height: 1200px;
  }
  .sandwich-board {
    position: absolute;
    left: 20px;
    top: 169px;
    width: 680px;
    height: 862px;
    box-shadow: 0 14px 34px rgba(0,0,0,0.22);
  }
  .sandwich-board svg { display: block; width: 100%; height: 100%; }
  .serif { font-family: "Noto Serif", Georgia, serif; }
  .sans { font-family: "Source Sans 3", "Helvetica Neue", Arial, sans-serif; }
</style>
</head>
<body>
<main class="canvas">
  <section class="sandwich-board" aria-label="Brightstep Foot Care sandwich board">
    <svg viewBox="0 0 820 1040" xmlns="http://www.w3.org/2000/svg">
      <defs>
        <linearGradient id="photo-tone" x1="0" y1="0" x2="1" y2="1">
          <stop offset="0" stop-color="var(--photo-light)"/>
          <stop offset="0.55" stop-color="var(--photo-skin)"/>
          <stop offset="1" stop-color="var(--photo-light)"/>
        </linearGradient>
        <linearGradient id="pill-tone" x1="0" y1="0" x2="0" y2="1">
          <stop offset="0" stop-color="var(--pill-grey-light)"/>
          <stop offset="1" stop-color="var(--pill-grey)"/>
        </linearGradient>
      </defs>

      <!-- blue field -->
      <rect class="board-field" width="820" height="1040" fill="var(--brand-blue)"/>

      <!-- grey swoosh edge -->
      <path class="swoosh-edge" fill="var(--swoosh-grey)"
        d="M310,0 C240,80 268,200 328,330 C398,470 478,600 508,800 C528,950 580,1025 700,1040 L820,1040 L820,0 Z"/>
      <!-- white panel -->
      <path class="photo-panel" fill="var(--paper)"
        d="M332,0 C262,80 290,200 350,330 C420,470 500,600 530,800 C550,950 610,1020 740,1040 L820,1040 L820,0 Z"/>

      <!-- photo area -->
      <path class="photo-area" role="img" aria-label="Photo of smooth bare legs and feet on tiptoe, with a hand resting on the calf"
        fill="url(#photo-tone)" opacity="0.75"
        d="M372,0 C310,80 332,200 390,330 C460,470 540,600 570,800 L820,800 L820,0 Z"/>

      <!-- brochure holder slot -->
      <rect class="brochure-slot" x="345" y="55" width="130" height="33" rx="16.5"
        fill="var(--paper)" stroke="#9a9a9a" stroke-width="1.5"/>

      <!-- offer badge -->
      <g class="offer-badge">
        <circle cx="205" cy="153" r="100" fill="none" stroke="var(--paper)" stroke-width="2"/>
        <circle cx="208" cy="153" r="94" fill="var(--paper)"/>
        <text class="serif" text-anchor="middle" fill="var(--ink)" font-size="30">
          <tspan x="194" y="117">visit</tspan>
          <tspan x="206" y="142">now for</tspan>
        </text>
        <text class="serif" text-anchor="middle" fill="var(--brand-blue)" font-size="37" font-weight="700">
          <tspan x="206" y="174">exciting</tspan>
          <tspan x="206" y="208">offers</tspan>
        </text>
      </g>

      <!-- headline -->
      <text class="serif headline" fill="var(--paper)" text-anchor="middle">
        <tspan x="186" y="346" font-size="78">Your</tspan>
        <tspan x="194" y="418" font-size="80" font-weight="700">Fungal</tspan>
        <tspan x="198" y="500" font-size="78">Nail</tspan>
        <tspan x="212" y="568" font-size="80" font-weight="700">Experts</tspan>
      </text>

      <!-- brand name -->
      <g class="brand-name">
        <circle cx="238" cy="682" r="64" fill="none" stroke="var(--paper)" stroke-width="6"/>
        <text class="serif" fill="var(--paper)" font-size="38" text-anchor="middle" letter-spacing="4">
          <tspan x="238" y="808">BRIGHTSTEP</tspan>
          <tspan x="238" y="854">FOOT CARE</tspan>
        </text>
      </g>

      <!-- phone -->
      <g class="contact-phone">
        <circle cx="89" cy="910" r="24" fill="none" stroke="var(--paper)" stroke-width="4"/>
        <circle cx="89" cy="910" r="17" fill="var(--paper)"/>
        <path fill="var(--brand-blue)"
          d="M82,898 l5,0 l2,7 l-3,2 c1.5,3.5 4,6 7.5,7.5 l2,-3 l7,2 l0,5 c-12,1 -22,-9 -21,-21 z"/>
        <text class="sans" x="128" y="930" fill="var(--paper)" font-size="54" font-weight="600">(07) 312 5840</text>
      </g>

      <!-- website -->
      <g class="contact-web">
        <rect x="63" y="954" width="370" height="42" rx="21" fill="var(--black)"/>
        <text class="sans" x="248" y="984" fill="var(--paper)" font-size="28" font-weight="600" text-anchor="middle">BrightstepFootCare.co.nz</text>
      </g>

      <!-- treatment list -->
      <g class="treatments sans" font-size="30" font-weight="600" fill="var(--paper)">
        <g class="treatment">
          <rect x="515" y="700" width="242" height="40" rx="20" fill="url(#pill-tone)"/>
          <circle cx="510" cy="720" r="26" fill="#b74e7d" stroke="var(--paper)" stroke-width="2" role="img" aria-label="Cold laser device photo"/>
          <text x="553" y="731">COLD LASER</text>
        </g>
        <g class="treatment">
          <rect x="527" y="760" width="230" height="40" rx="20" fill="url(#pill-tone)"/>
          <circle cx="521" cy="780" r="26" fill="#e6c3ad" stroke="var(--paper)" stroke-width="2" role="img" aria-label="Topical treatment photo"/>
          <text x="565" y="791">TOPICAL</text>
        </g>
        <g class="treatment">
          <rect x="515" y="820" width="242" height="40" rx="20" fill="url(#pill-tone)"/>
          <circle cx="509" cy="840" r="26" fill="#9fd0cc" stroke="var(--paper)" stroke-width="2" role="img" aria-label="Oral tablets photo"/>
          <text x="553" y="851">ORAL</text>
        </g>
        <g class="treatment">
          <rect x="503" y="880" width="254" height="40" rx="20" fill="url(#pill-tone)"/>
          <circle cx="497" cy="900" r="26" fill="#e7e3e0" stroke="var(--paper)" stroke-width="2" role="img" aria-label="Nail surgery photo"/>
          <text x="541" y="911">SURGERY</text>
        </g>
        <g class="treatment">
          <rect x="509" y="940" width="248" height="40" rx="20" fill="url(#pill-tone)"/>
          <circle cx="503" cy="960" r="26" fill="#a9a3dc" stroke="var(--paper)" stroke-width="2" role="img" aria-label="Nail care photo"/>
          <text x="547" y="971">NAIL CARE</text>
        </g>
      </g>
    </svg>
  </section>
</main>
</body>
</html>
```